Flyer for American Indian Elders on Dementia Warning Signs

We need a flyer designed for older adults who are American Indian or Alaska Native (in the U.S.).

Ideally, the flyer should complement the colors of our logos. The project logo and our organization logo are attached to the brief.

When people see the flyer we want them to feel that it represents their culture, is warm, and professional but relatable to older adults and people who have limited incomes.

I have attached an earlier draft of the document we designed ourselves BUT we want different and better.

It is for older adults who have trouble reading so:
1. you must use a font that is 11.5 points or larger
2. Do not put text over complex pictures or use shading with words
3. You can use a serif font for the heading, but should use san serif for the body text
4. There should be good contrast between the font color and background

Please do not use any images that include a head dress or pictures of American Indian people or things that are very traditional or "token" imagery.

We need to save a small space under the call out box/ somewhere on the flyer for other people to add their logo once they download.

Let us know if you have questions or need additional information.

Target Market(s)

Older American Indian people

Font styles to use
Serif
Sans Serif

Requirements
Must have
• Easy to read for older adults
Should not have
• indian headdress

```html
<!DOCTYPE html>
<html lang="en">
<head>
<meta charset="utf-8">
<title>10 Signs of Thinking or Memory Changes that Might be Dementia</title>
<link rel="stylesheet" href="https://fonts.googleapis.com/css2?family=Gilda+Display&family=Inter+Tight:ital,wght@0,400;0,600;0,700;1,400;1,600&display=swap">
<style>
  :root{
    --rust:#a9605a;
    --rust-deep:#b0534b;
    --teal:#4fa6ab;
    --teal-soft:#6fb0b3;
    --ink:#2f2f33;
    --blush:#fcf1f0;
    --paper:#ffffff;
    --backdrop:#b3b3b3;
  }
  *{box-sizing:border-box;margin:0;padding:0}
  html,body{width:1009px;height:1200px;overflow:hidden;background:var(--backdrop)}
  body{font-family:"Inter Tight",sans-serif;color:var(--ink);letter-spacing:-0.02em}
  .flyer{position:absolute;left:84px;top:6px;width:840px;height:1188px;background:var(--paper);overflow:hidden}

  /* header */
  .brand{position:absolute;display:flex;align-items:center;gap:10px}
  .brand-primary{left:37px;top:21px;height:80px}
  .brand-primary .mark{width:80px;height:80px;border-radius:50%;background:var(--teal);flex:none}
  .brand-primary .name{font-weight:700;color:var(--teal);font-size:19px;line-height:21px;width:220px;letter-spacing:-0.01em}
  .divider{position:absolute;left:358px;top:22px;width:1px;height:84px;background:var(--rust)}
  .brand-partner{left:370px;top:28px;width:110px;flex-direction:column;align-items:flex-start;gap:6px}
  .brand-partner .mark{width:44px;height:44px;background:var(--teal)}
  .brand-partner .name{font-weight:700;color:var(--rust);font-size:10px;line-height:12px;letter-spacing:0}

  /* banner */
  .banner{position:absolute;left:0;top:115px;width:840px;height:178px;background:linear-gradient(90deg,var(--rust) 0%,#8a7f7c 50%,var(--teal-soft) 100%)}
  .headline{position:absolute;left:37px;top:128px;font-family:"Gilda Display",serif;font-weight:400;color:#fff;font-size:46px;line-height:53px;letter-spacing:-0.03em}
  .headline .highlight{background:var(--teal);padding:0 4px}
  .illustration{position:absolute;left:490px;top:16px;width:320px;height:277px;border-radius:40% 40% 0 0;background:linear-gradient(160deg,#f2a38f 0%,#c8615a 55%,#e9e9e9 100%)}

  /* intro */
  .intro{position:absolute;left:37px;top:308px;width:760px;font-size:15.5px;line-height:20px}
  .intro p+p{margin-top:6px}
  .intro .ask{font-weight:700;color:var(--rust-deep)}
  .intro .act{font-weight:600;color:var(--teal)}

  /* signs */
  .col-bg{position:absolute;left:420px;top:413px;width:420px;height:484px;background:var(--blush)}
  .feather-faint{position:absolute;left:764px;top:533px;width:76px;height:165px;border-radius:60% 0 0 60%;background:linear-gradient(200deg,rgba(79,166,171,.55),rgba(79,166,171,.08))}
  .signs{position:absolute;top:432px;list-style:none;font-size:15.5px;line-height:19.6px}
  .signs-left{left:37px;width:350px}
  .signs-right{left:450px;width:370px}
  .sign{margin-bottom:12px}
  .sign-title{display:block;padding-left:17px;text-indent:-17px}
  .sign-title b{font-weight:700}
  .sign ul{list-style:none}
  .sign li{position:relative;padding-left:16px}
  .sign li::before{content:"›";position:absolute;left:0;top:-1px;font-size:18px}
  .signs-left .sign:nth-child(2){margin-top:0}
  .signs-right .sign{margin-bottom:14px}

  /* bottom */
  .note{position:absolute;left:0;top:897px;width:420px;height:274px;background:linear-gradient(90deg,var(--rust) 0%,#8a7f7c 55%,var(--teal-soft) 100%)}
  .feather{position:absolute;left:7px;top:1032px;width:112px;height:139px;display:none}
  .feather-main{position:absolute;left:7px;top:878px;width:112px;height:293px;border-radius:50% 50% 45% 45%;background:linear-gradient(180deg,#3b3a5a 0%,#a2643a 35%,#f2ead8 70%,#d8d2c8 100%)}
  .note-text{position:absolute;left:123px;top:916px;width:285px;color:#fff;font-size:15.5px;line-height:20px}
  .note-text p+p{margin-top:7px}
  .note-text b{font-weight:700}

  .callout{position:absolute;left:420px;top:897px;width:420px;height:128px;background:var(--rust)}
  .callout::after{content:"";position:absolute;left:190px;bottom:-24px;border-left:20px solid transparent;border-right:20px solid transparent;border-top:25px solid var(--rust)}
  .callout-title{position:absolute;left:30px;top:30px;width:360px;color:#fff;font-weight:700;font-size:15.5px;line-height:20px}
  .callout-links{position:absolute;left:30px;top:80px;color:#fff;font-style:italic;font-size:16.5px}
  .logo-slot{position:absolute;left:420px;top:1093px;width:420px;text-align:center;color:var(--rust-deep);font-weight:600;font-size:16px}

  .foot{position:absolute;left:0;top:1171px;width:840px;height:17px;background:var(--teal)}
</style>
</head>
<body>
<main class="flyer">
  <header>
    <div class="brand brand-primary">
      <span class="mark"></span>
      <span class="name">Native Elders Brain Health Center</span>
    </div>
    <span class="divider"></span>
    <div class="brand brand-partner">
      <span class="mark"></span>
      <span class="name">Circle of Indigenous Elders Network</span>
    </div>
  </header>

  <section class="banner"></section>
  <div class="illustration" role="img" aria-label="Illustration of an older man holding his head, surrounded by puzzle pieces and question marks"></div>
  <h1 class="headline">10 Signs of Thinking or<br>Memory Changes that<br>Might be <span class="highlight">DEMENTIA!</span></h1>

  <section class="intro">
    <p>As we get older, we may slow down a bit. This is a normal part of aging. Changes in memory or thinking that make it harder to get through the day, are not a normal part of aging. These may be early signs of dementia.</p>
    <p>Because American Indian and Alaska Native people have a high risk of dementia, it is important to know the warning signs. <span class="ask">Do you have any of these 10 signs?</span> <span class="act">If so, talk to your doctor.</span></p>
  </section>

  <div class="col-bg"></div>
  <div class="feather-faint" role="img" aria-label="Soft teal feather decoration"></div>

  <ol class="signs signs-left">
    <li class="sign"><span class="sign-title"><b>1.&nbsp; Memory loss that affects your daily life.</b> You may:</span>
      <ul><li>Forget events or important dates</li><li>Repeat yourself</li><li>Rely more often on lists /sticky notes to remember things</li></ul></li>
    <li class="sign"><span class="sign-title"><b>2. Trouble planning or solving problems.</b><br>You may have harder time:</span>
      <ul><li>Paying bills</li><li>Cooking recipes you have used for years</li></ul></li>
    <li class="sign"><span class="sign-title"><b>3. Daily tasks are getting harder,</b> including:</span>
      <ul><li>Driving</li><li>Making a grocery list or going shopping</li></ul></li>
    <li class="sign"><span class="sign-title"><b>4.&nbsp; Trouble with how your eyesight and thinking work together that gets worse.</b> This includes:</span>
      <ul><li>Tripping, falls, or problems with your balance</li><li>Spilling or dropping things more</li></ul></li>
    <li class="sign"><span class="sign-title"><b>5.&nbsp; New trouble talking or writing.</b> You have a hard time finding the words you want to say. For example, you may say “that thing on your wrist that tells time” instead of “watch.”</span></li>
  </ol>

  <ol class="signs signs-right">
    <li class="sign"><span class="sign-title"><b>6.&nbsp; Get confused about the time, date, or where you are.</b></span></li>
    <li class="sign"><span class="sign-title"><b>7.&nbsp; Lose and cannot find things.</b> For example, you:</span>
      <ul><li>Can’t find the coffee pot that you use every day</li><li>Might put your car keys in the freezer</li></ul></li>
    <li class="sign"><span class="sign-title"><b>8. Notice changes in mood or personality,</b><br>such as being:</span>
      <ul><li>Easily mad or sad in everyday situations</li><li>More fearful (scared) or suspicious (not trusting)</li></ul></li>
    <li class="sign"><span class="sign-title"><b>9.&nbsp; Act different and make poor choices.</b> This may make you more likely to:</span>
      <ul><li>Spend money you do not have or be a scam victim</li><li>Stop washing up regularly or pay less attention to how you look</li><li>Forget to take care of your pet</li></ul></li>
    <li class="sign"><span class="sign-title"><b>10.&nbsp; Pull away from friends and family because it is harder to keep up.</b> You may not want to do things you used to enjoy, like sporting events, church, music, or sex.</span></li>
  </ol>

  <section class="note"></section>
  <div class="feather-main" role="img" aria-label="Brown and cream feather"></div>
  <div class="note-text">
    <p><b>American Indian</b> and <b>Alaska Native</b> people have a high risk of <b>dementia.</b></p>
    <p>Big changes in memory or thinking that make it hard to get through the day are not a normal part of aging.</p>
    <p>People with one or more of these <b>10 signs</b> should talk to their doctor to find the cause. It is not always dementia.</p>
    <p>Early <b>dementia diagnosis</b> gives you a chance to get care and plan your future.</p>
  </div>

  <section class="callout">
    <p class="callout-title">To learn more about the warning signs of dementia in American Indian and Alaska Native people, visit:</p>
    <p class="callout-links">www.nativeeldersmind.org | www.healthyagingpath.org</p>
  </section>
  <p class="logo-slot">Logo Here</p>

  <div class="foot"></div>
</main>
</body>
</html>
```